Visitenkarten für eine Hypnose-Praxis
Ich bin sehr zufrieden mit der professionellen Arbeitsweise von KOR7342. Es war immer ein netter Kontakt und meine Wünsche wurden schnell umgesetzt. Alle Vorschläge waren sehr kreativ und und so viel es mir leicht, eine schnelle Entscheidung zu treffen.
Zielgruppe
Wir sind eine Hypnose-Praxis und richten unser Angebot an Privatpersonen unterschiedlichen Alters, die therapeutische Unterstützung suchen.
Aufgabenstellung
Eher schlichtes und modernes Design

```html
<!DOCTYPE html>
<html lang="de">
<head>
<meta charset="utf-8">
<title>Nachtruhe – Visitenkarten</title>
<link href="https://fonts.googleapis.com/css2?family=Montserrat:wght@300;400;500&display=swap" rel="stylesheet">
<style>
  :root {
    --stage: #2f2b2b;
    --paper: #fbfbfa;
    --ink: #232323;
    --ink-soft: #555;
    --green: #3fa44a;
    --green-dark: #2f8a3b;
    --teal: #2bb3a6;
    --blue: #3a9fd6;
    --swirl-blue: #cfe9f2;
    --swirl-green: #e3f1d9;
  }
  * { margin: 0; padding: 0; box-sizing: border-box; }
  html, body {
    width: 1200px; height: 900px; overflow: hidden;
    background: var(--stage);
    font-family: "Montserrat", sans-serif;
    color: var(--ink);
  }
  .stage {
    width: 1200px; height: 900px;
    display: flex; align-items: center; justify-content: center; gap: 70px;
  }
  .card {
    position: relative;
    width: 340px; height: 525px;
    background: var(--paper);
    box-shadow: 0 20px 40px rgba(0,0,0,.35);
    overflow: hidden;
  }
  /* front */
  .card-front .swirl-art {
    position: absolute; top: 0; right: 0;
    width: 300px; height: 250px;
    background: radial-gradient(ellipse at 85% 55%, var(--swirl-green) 0%, var(--swirl-blue) 45%, rgba(255,255,255,0) 75%);
  }
  .brand {
    position: absolute;
    display: flex; align-items: flex-start; gap: 10px;
  }
  .card-front .brand { left: 34px; top: 330px; }
  .card-back .brand { left: 34px; top: 48px; }
  .brand-mark {
    width: 30px; height: 30px; margin-top: 8px;
    background: var(--teal); border-radius: 4px;
  }
  .brand-name {
    font-size: 44px; font-weight: 500; line-height: 1; color: var(--ink);
    letter-spacing: -.5px;
  }
  .brand-tagline {
    font-size: 10px; font-weight: 400; letter-spacing: 3px;
    color: var(--ink-soft); margin-top: 8px; text-transform: uppercase;
  }
  /* back */
  .card-back .person {
    position: absolute; right: 30px; top: 175px; text-align: right;
  }
  .person-name {
    font-size: 19px; font-weight: 300; letter-spacing: 4px;
    text-transform: uppercase; color: var(--ink-soft);
  }
  .person-role {
    margin-top: 16px; font-size: 9.5px; line-height: 1.45;
    text-transform: uppercase; color: var(--ink);
  }
  .contact {
    position: absolute; right: 30px; bottom: 34px; text-align: right;
    font-size: 12px; line-height: 1.55; color: var(--ink);
  }
  .contact .address { margin-bottom: 10px; }
  .contact-icons {
    position: absolute; left: 0; bottom: 34px;
    display: flex; flex-direction: column;
  }
  .contact-icon {
    width: 40px; height: 40px; display: flex; align-items: center; justify-content: center;
  }
  .contact-icon svg { width: 22px; height: 22px; fill: none; stroke: #fff; stroke-width: 2; stroke-linecap: round; stroke-linejoin: round; }
  .icon-pin { background: var(--green); }
  .icon-phone { background: var(--green-dark); }
  .icon-mail { background: var(--teal); }
  .icon-web { background: var(--blue); }
</style>
</head>
<body>
<main class="stage">
  <section class="card card-front">
    <div class="swirl-art" role="img" aria-label="Feine blaugrüne Spirallinien als Hypnose-Motiv"></div>
    <div class="brand">
      <div class="brand-mark"></div>
      <div>
        <div class="brand-name">Nachtruhe</div>
        <div class="brand-tagline">Hypnose-Therapie</div>
      </div>
    </div>
  </section>

  <section class="card card-back">
    <div class="brand">
      <div class="brand-mark"></div>
      <div>
        <div class="brand-name">Nachtruhe</div>
        <div class="brand-tagline">Hypnose-Therapie</div>
      </div>
    </div>

    <div class="person">
      <div class="person-name">Lena Vormholt</div>
      <div class="person-role">
        Diplom-Psychologin,<br>
        Heilpraktikerin für Psychotherapie<br>
        mit Spezialisierung Hypnose-Therapie
      </div>
    </div>

    <div class="contact-icons">
      <div class="contact-icon icon-pin">
        <svg viewBox="0 0 24 24"><path d="M12 21s-6-6.2-6-11a6 6 0 0 1 12 0c0 4.8-6 11-6 11z"/><circle cx="12" cy="10" r="2.2"/></svg>
      </div>
      <div class="contact-icon icon-phone">
        <svg viewBox="0 0 24 24"><path d="M5 3h4l2 5-2.5 1.5a11 11 0 0 0 6 6L16 13l5 2v4a2 2 0 0 1-2 2A16 16 0 0 1 3 5a2 2 0 0 1 2-2z"/></svg>
      </div>
      <div class="contact-icon icon-mail">
        <svg viewBox="0 0 24 24"><rect x="3" y="5" width="18" height="14" rx="1"/><path d="M3 6l9 7 9-7"/></svg>
      </div>
      <div class="contact-icon icon-web">
        <svg viewBox="0 0 24 24"><circle cx="12" cy="12" r="9"/><path d="M3 12h18M12 3c3 3 3 15 0 18M12 3c-3 3-3 15 0 18"/></svg>
      </div>
    </div>

    <div class="contact">
      <div class="address">Birkenweg 14<br>12045 Berlin</div>
      <div>Tel: 030 55 18 42 07</div>
      <div>24-Std-AB: 030 61 39 27 50</div>
      <div>info@nachtruhe-hypnose.de</div>
      <div>www.nachtruhe-hypnose.de</div>
    </div>
  </section>
</main>
</body>
</html>
```